Art Wall - Illustrates "Be Colorful"

I have a seasonal color business called Porch Step Blooms. We plant containers and add colorful annuals to garden beds. I need a 6' tall by 18' long banner that will be hung on a wall or possibly used on the side of my enclosed trailer. The banner will be used as backdrop for ladies taking pictures together and as a backdrop for colorful container gardens to be photographed for our website. It should have the words "Be Colorful" on it. I would like for it to look like a fun art wall that you would take a picture in front of in a downtown area. The art should work well with our logo. We love flowers but other ideas are welcome. Feel free to look at our instagram @porchstepbloomsokc to see examples of our work. I have uploaded our logo and a colorful flower picture we liked (great colors) but didn't quite work with our logo and a fun colorful wall at a restaurant that we really like.

Target Market(s)

women ages 30-45, wealthy, like to feel like they are trendy

Industry/Entity Type

Landscape Gardening

Font styles to use
Serif

Requirements
Must have
• The words "Be Colorful" on it and some space that would good for people to stand or objects to be placed to be photographed.
Nice to have
• We really like the colors in the "sun's out now" t-shirt picture I have attached. Also like the watercolor, alcohol ink, or hand-painted look.
Should not have
• Please do not include our logo on the banner. It will be added as a watermark to our photos.

Please do not literally use the logo flower in the design. Feel free to use pieces or inspiration from the logo but the wall should look more like art and less like a cartoon.

```html
<!DOCTYPE html>
<html lang="en">
<head>
<meta charset="utf-8">
<title>Be Colorful – Art Wall Options</title>
<link rel="stylesheet" href="https://fonts.googleapis.com/css2?family=Graduate&family=Open+Sans:wght@400&display=swap">
<style>
  :root {
    --page: #ffffff;
    --label: #111111;
    --ink-outline: #1c1c1c;
    --shadow: rgba(40, 30, 20, 0.55);
    --olive: #9f9570;
    --olive-dark: #6f6437;
    --sage: #b9b9a2;
    --sand: #f2cf8f;
    --apricot: #eeae6c;
    --rose: #e8857f;
    --coral: #f24c5e;
    --brick: #b8584a;
    --white: #ffffff;
    --lime: #88ff00;
    --yellow: #ffe800;
    --orange: #ff5a00;
    --crimson: #c40000;
    --magenta: #ff00ff;
    --violet: #9a33ff;
    --blue: #3366ff;
    --cyan: #44ddff;
  }
  html, body {
    margin: 0;
    width: 1200px;
    height: 996px;
    overflow: hidden;
    background: var(--page);
  }
  .sheet {
    position: relative;
    width: 1200px;
    height: 996px;
  }
  .option-label {
    position: absolute;
    left: 133px;
    margin: 0;
    font-family: "Open Sans", Arial, sans-serif;
    font-size: 15px;
    font-weight: 400;
    color: var(--label);
    letter-spacing: 0.2px;
  }
  .option-label--one { top: 86px; }
  .option-label--two { top: 539px; }
  .banner {
    position: absolute;
    left: 133px;
    width: 961px;
    height: 320px;
    overflow: hidden;
  }
  .banner--one { top: 123px; }
  .banner--two { top: 576px; }
  .banner__art {
    position: absolute;
    inset: 0;
    background:
      linear-gradient(to right,
        var(--olive) 0%, var(--sage) 3%, var(--apricot) 6%, var(--sand) 10%,
        var(--rose) 15%, var(--coral) 18%, var(--brick) 21%, var(--sage) 25%,
        var(--olive) 28%, var(--sand) 33%, var(--rose) 39%, var(--brick) 43%,
        var(--sand) 48%, var(--olive) 53%, var(--sand) 58%, var(--apricot) 62%,
        var(--sage) 65%, var(--coral) 70%, var(--rose) 74%, var(--olive) 78%,
        var(--sand) 83%, var(--brick) 88%, var(--rose) 92%, var(--sand) 96%, var(--olive) 100%);
  }
  .headline {
    position: absolute;
    margin: 0;
    font-family: "Graduate", Georgia, serif;
    font-weight: 400;
    line-height: 1;
    white-space: nowrap;
    -webkit-text-stroke: 1.5px var(--ink-outline);
    text-shadow: 6px 8px 8px var(--shadow);
  }
  .banner--one .headline {
    left: 50%;
    top: 122px;
    transform: translateX(-50%);
    font-size: 74px;
    letter-spacing: -3px;
  }
  .banner--two .headline {
    left: 48px;
    top: 117px;
    font-size: 86px;
    letter-spacing: -3.5px;
  }
  .l-white { color: var(--white); }
  .l-lime { color: var(--lime); }
  .l-yellow { color: var(--yellow); }
  .l-orange { color: var(--orange); }
  .l-crimson { color: var(--crimson); }
  .l-magenta { color: var(--magenta); }
  .l-violet { color: var(--violet); }
  .l-blue { color: var(--blue); }
  .l-cyan { color: var(--cyan); }
</style>
</head>
<body>
<main class="sheet">
  <p class="option-label option-label--one">OPTION 1</p>
  <section class="banner banner--one">
    <div class="banner__art" role="img" aria-label="Hand-painted watercolor wall of wavy vertical ribbons in olive, sand, apricot, rose and coral"></div>
    <h1 class="headline"><span class="l-white">BE</span> <span class="l-lime">C</span><span class="l-yellow">O</span><span class="l-orange">L</span><span class="l-crimson">O</span><span class="l-magenta">R</span><span class="l-violet">F</span><span class="l-blue">U</span><span class="l-cyan">L</span></h1>
  </section>

  <p class="option-label option-label--two">OPTION 2</p>
  <section class="banner banner--two">
    <div class="banner__art" role="img" aria-label="Hand-painted watercolor wall of wavy vertical ribbons in olive, sand, apricot, rose and coral"></div>
    <h2 class="headline"><span class="l-white">BE</span> <span class="l-lime">C</span><span class="l-yellow">O</span><span class="l-orange">L</span><span class="l-crimson">O</span><span class="l-magenta">R</span><span class="l-violet">F</span><span class="l-blue">U</span><span class="l-cyan">L</span></h2>
  </section>
</main>
</body>
</html>
```